Website that informs user about the Darknet

A short 1 pager website that explains what the darknet is.
Current site: https://velmora.gs/ & https://quintaro.kr/. No logo needed. Just an informational page. Choose the layout / colours that you prefer.

Target Market(s)

Endusers, companies etc.

Coding

Coded - Design and coding required

Number of Pages Required

1 page

Requirements
Must have
• 1 Small contact form - thats all
Should not have
• The page must look professional. Not for kids. I target mainly adults / employees

```html
<!DOCTYPE html>
<html lang="en">
<head>
<meta charset="utf-8">
<title>The Darknet</title>
<link href="https://fonts.googleapis.com/css2?family=Roboto:ital,wght@0,300;0,400;0,500;0,700;0,900;1,900&display=swap" rel="stylesheet">
<style>
:root{
  --navy:#06122b;
  --blue:#0aa4e8;
  --ink:#161616;
  --muted:#777;
  --link:#0d4f8f;
  --light:#f3f4f6;
  --grey:#dcdcdc;
  --foot:#0b0b0c;
  --white:#fff;
}
*{margin:0;padding:0;box-sizing:border-box}
html,body{width:1200px;height:3008px;overflow:hidden}
body{position:relative;font-family:'Roboto',Arial,sans-serif;color:var(--ink);background:var(--white)}
.abs{position:absolute}

/* hero */
.hero{left:0;top:0;width:1200px;height:650px;background:radial-gradient(circle at 78% 45%,#2f6f86 0%,#123846 30%,#06171d 70%,#030b0e 100%)}
.brand{left:99px;top:22px;font-size:34px;font-weight:500;color:var(--white)}
.menu{left:1004px;top:30px;color:var(--white);font-size:21px;display:flex;align-items:center;gap:14px}
.welcome-band{left:215px;top:196px;width:493px;height:88px;background:var(--navy);transform:skewX(-8deg)}
.title-band{left:100px;top:290px;width:548px;height:90px;background:var(--blue);transform:skewX(-8deg)}
.hero-line{font-style:italic;font-weight:900;color:var(--white);font-size:68px;letter-spacing:-1px;line-height:1}
.hero-line.one{left:252px;top:206px}
.hero-line.two{left:145px;top:300px}
.scroll{left:584px;top:574px}

/* access */
.access{left:0;top:650px;width:1200px;height:645px;background:var(--light)}
.section-title{font-size:29px;font-weight:500;text-transform:uppercase}
.access .section-title{left:0;width:1200px;text-align:center;top:90px}
.card{width:320px;text-align:center}
.card svg{display:block;margin:0 auto}
.card h3{font-size:25px;font-weight:400;text-transform:uppercase;line-height:1.25;margin-top:24px}
.card p{font-size:15px;color:var(--muted);line-height:26px;margin-top:16px;font-weight:300}
.card.c1{left:101px;top:230px}
.card.c2{left:441px;top:230px}
.card.c3{left:778px;top:230px}
.card.featured-frame{left:442px;top:173px;width:324px;height:374px;border:2px dashed #222}
.btn-more{width:134px;height:44px;background:#000;color:var(--white);font-size:15px;font-weight:500;display:flex;align-items:center;justify-content:center;clip-path:polygon(8% 0,100% 0,92% 100%,0 100%)}
.b1{left:183px;top:513px}.b2{left:527px;top:513px}.b3{left:862px;top:513px}

/* understand */
.understand{left:0;top:1295px;width:1200px;height:758px;background:linear-gradient(110deg,#efefef 0%,#dedede 55%,#cfd2d6 100%)}
.shield-art{left:640px;top:0;width:560px;height:758px;background:radial-gradient(circle at 72% 48%,#1d4f86 0%,#5e7d9b 22%,#b6c0ca 45%,rgba(220,220,220,0) 70%)}
.understand .section-title{left:98px;top:62px;font-size:30px}
.point{width:400px}
.point .num{position:absolute;left:-42px;top:-5px;width:32px;height:32px;border:2px solid #333;border-radius:50%;font-size:14px;font-weight:500;display:flex;align-items:center;justify-content:center}
.point h4{font-size:15px;color:var(--link);font-weight:500}
.point p{font-size:11px;line-height:18px;margin-top:7px;color:#222}
.p1{left:285px;top:140px;width:380px}
.p2-box{left:153px;top:273px;width:446px;height:146px;background:var(--white);border-radius:4px;box-shadow:0 2px 8px rgba(0,0,0,.2)}
.p2{left:208px;top:292px;width:376px}
.p2 a{color:var(--link)}
.p3{left:174px;top:452px;width:380px}
.p4{left:251px;top:602px;width:365px}

/* contact */
.contact{left:0;top:2053px;width:1200px;height:535px;background:linear-gradient(#fff,#fff)}
.contact .section-title{left:0;width:1200px;text-align:center;top:96px;font-size:30px}
.contact-photo{left:174px;top:183px;width:368px;height:352px;background:linear-gradient(160deg,#1d2a22 0%,#0c120f 55%,#2b2b2b 100%)}
.form{left:542px;top:183px;width:471px;height:352px;background:#f2f2f2}
.field{position:absolute;left:35px;width:408px;border-bottom:1px solid #aaa;font-size:11px;color:#444}
.f-name{top:30px;height:22px}.f-mail{top:88px;height:22px}.f-msg{top:134px;height:86px}
.send{position:absolute;left:156px;top:243px;width:135px;height:43px;background:var(--blue);color:var(--white);font-size:17px;font-weight:500;display:flex;align-items:center;justify-content:center}

/* footer */
.footer{left:0;top:2540px;width:1200px;height:468px}
.footer-bg{left:0;top:0}
.f-brand{left:99px;top:165px;font-size:34px;font-weight:500;color:var(--white)}
.f-social-title{left:97px;top:240px;font-size:26px;color:var(--white)}
.socials{left:97px;top:296px;display:flex;gap:36px}
.socials span{width:20px;height:20px;border-radius:50%;background:var(--white)}
.f-head{top:92px;font-size:21px;color:var(--white);text-transform:uppercase}
.h-quick{left:371px}.h-contact{left:539px}.h-sub{left:796px}
.f-links{left:372px;top:145px;color:var(--white);font-size:16px;line-height:30px;list-style:none}
.f-contact{left:535px;top:144px;color:var(--white);font-size:16px;line-height:26px;width:200px}
.f-contact .row{display:flex;gap:14px;margin-bottom:10px}
.f-contact svg{flex:none;margin-top:5px}
.f-sub-text{left:790px;top:138px;width:340px;color:var(--white);font-size:16px;line-height:26px}
.f-input{left:790px;top:204px;width:324px;height:44px;border:1px solid #777;border-radius:4px;color:var(--white);font-size:15px;padding:12px 12px}
.f-input .divider{position:absolute;left:269px;top:10px;width:1px;height:24px;background:#aaa}
.f-input svg{position:absolute;left:285px;top:13px}
.f-rule{left:0;top:393px;width:1200px;height:1px;background:#444}
.copyright{left:0;top:426px;width:1200px;text-align:center;color:var(--white);font-size:15px}
</style>
</head>
<body>

<header class="abs hero" role="img" aria-label="Hooded figure in front of glowing green code rain">
  <div class="abs brand">The Darknet</div>
  <div class="abs menu">MENU
    <svg width="22" height="18" viewBox="0 0 22 18" fill="#fff"><rect y="0" width="22" height="3"/><rect y="5" width="22" height="3"/><rect y="10" width="22" height="3"/><rect y="15" width="22" height="3"/></svg>
  </div>
  <div class="abs welcome-band"></div>
  <div class="abs title-band"></div>
  <h1 class="abs hero-line one">WELCOME TO</h1>
  <div class="abs hero-line two">THE DARKNET</div>
  <svg class="abs scroll" width="32" height="56" viewBox="0 0 32 56" fill="none" stroke-width="4">
    <path d="M4 4l12 12 12-12" stroke="#fff"/><path d="M4 20l12 12 12-12" stroke="#fff"/><path d="M4 36l12 12 12-12" stroke="#8b95a0"/>
  </svg>
</header>

<section class="abs access">
  <h2 class="abs section-title">Accessing the Darknet</h2>
  <div class="abs featured-frame"></div>

  <div class="abs card c1">
    <svg width="110" height="110" viewBox="0 0 110 110" fill="none" stroke="#1c2a55" stroke-width="3">
      <rect x="4" y="4" width="102" height="102" rx="6"/><line x1="4" y1="26" x2="106" y2="26"/>
      <circle cx="16" cy="15" r="3"/><circle cx="27" cy="15" r="3"/><circle cx="38" cy="15" r="3"/>
      <rect x="18" y="36" width="74" height="50" rx="3"/><rect x="36" y="92" width="38" height="8" rx="3"/>
    </svg>
    <h3>Veil Browser</h3>
    <p>Accessing the dark web can be done using a special browser called Veil. The Veil Browser is a web browser that</p>
  </div>

  <div class="abs card c2">
    <svg width="110" height="110" viewBox="0 0 110 110" fill="none" stroke="#1c2a55" stroke-width="3">
      <circle cx="55" cy="24" r="20"/><ellipse cx="55" cy="24" rx="9" ry="20"/><line x1="35" y1="24" x2="75" y2="24"/>
      <path d="M55 44l-18 20M55 44l18 20"/>
      <rect x="4" y="70" width="38" height="26" rx="2"/><rect x="68" y="70" width="38" height="26" rx="2"/>
      <line x1="42" y1="84" x2="68" y2="84"/><line x1="23" y1="96" x2="23" y2="104"/><line x1="87" y1="96" x2="87" y2="104"/>
    </svg>
    <h3>Proxies - Example<br>Shallot.ws</h3>
    <p>Shallot.ws is a darknet gateway or Veil2Web proxy. Simply replace .onion</p>
  </div>

  <div class="abs card c3">
    <svg width="110" height="110" viewBox="0 0 110 110" fill="none" stroke="#1c2a55" stroke-width="5">
      <circle cx="55" cy="55" r="51"/><circle cx="55" cy="55" r="22"/>
    </svg>
    <h3>Browser Extension</h3>
    <p>Onion search engine is an extension available for Glint Navigator that will allow the user of this browser to search</p>
  </div>

  <div class="abs btn-more b1">READ MORE</div>
  <div class="abs btn-more b2">READ MORE</div>
  <div class="abs btn-more b3">READ MORE</div>
</section>

<section class="abs understand">
  <div class="abs shield-art" role="img" aria-label="Shield with tick inside circular security rings"></div>
  <h2 class="abs section-title">Understand the Darknet</h2>

  <div class="abs point p1"><span class="num">01</span><h4>INTRODUCTION</h4>
    <p>The Dark Web is part of the Internet that cannot be indexed by regular search engines. Also, it is not possible to access the dark web with web browsers. Only by means of a special software (Veil Browser) it is possible to visit websites in the Darknet. The darknet is called "dark" only because of its anonymity. To understand what the dar</p></div>

  <div class="abs p2-box"></div>
  <div class="abs point p2"><span class="num">02</span><h4>UNDERSTAND THE INTERNET</h4>
    <p>The Internet is a network of computers that are linked together via a worldwide network. When someone sets up a web server with a website on the Internet, that website can be accessed by any computer or mobile device connected to the Internet. To do this, one uses a web browser such as Glint, Brisk Browser or many others. The websites a &nbsp;<a>+ Show More</a></p></div>

  <div class="abs point p3"><span class="num">03</span><h4>DARKNET VS. INTERNET</h4>
    <p>The Darknet is similar to the Internet, but there are significant differences. Similar to the Internet, the Darknet is only a network of computers (servers) that are connected to each other. Unlike the Internet, however, you can't access the websites with a regular web browser, for example, but with special software like the Veil Browser.</p></div>

  <div class="abs point p4"><span class="num">04</span><h4>IS THE DARKNET ILLIGAL?</h4>
    <p>Many think the darknet and access is crinimell. But this is not the case. The idea of the darknet comes from the desire to create anonymity. Therefore, the darknet makes sense for the exchange of protected business information or communication of political activists. Unfortunately, only criminal elements also seek anonymity. For example,</p></div>
</section>

<section class="abs contact">
  <h2 class="abs section-title">Contact Us</h2>
</section>

<footer class="abs footer">
  <svg class="abs footer-bg" width="1200" height="468" viewBox="0 0 1200 468">
    <path d="M0 52 Q600 -40 1200 52 V468 H0Z" fill="#0b0b0c"/>
    <rect y="393" width="1200" height="75" fill="#030303"/>
  </svg>
  <div class="abs f-brand">The Darknet</div>
  <div class="abs f-social-title">Social Media</div>
  <div class="abs socials" aria-label="Social media links"><span></span><span></span><span></span><span></span><span></span></div>

  <h3 class="abs f-head h-quick">Quick Link</h3>
  <ul class="abs f-links"><li>Home</li><li>About Us</li><li>Services</li><li>Contact Us</li></ul>

  <h3 class="abs f-head h-contact">Contact Us</h3>
  <div class="abs f-contact">
    <div class="row"><svg width="12" height="16" viewBox="0 0 12 16" fill="#fff"><path d="M6 0a6 6 0 0 0-6 6c0 4 6 10 6 10s6-6 6-10a6 6 0 0 0-6-6zm0 8a2 2 0 1 1 0-4 2 2 0 0 1 0 4z"/></svg><span>Lorem ipsum dolor sit amet, consectetur</span></div>
    <div class="row"><svg width="14" height="14" viewBox="0 0 14 14" fill="#fff"><path d="M3 0l3 3-2 2c1 2 3 4 5 5l2-2 3 3-2 3C6 13 1 8 0 2z"/></svg><span>+888-888-8888</span></div>
    <div class="row" style="margin-top:30px"><svg width="16" height="12" viewBox="0 0 16 12" fill="none" stroke="#fff" stroke-width="1.5"><rect x="1" y="1" width="14" height="10"/><path d="M1 1l7 6 7-6"/></svg><span style="margin-left:-2px">info@velmora-info.com</span></div>
  </div>

  <h3 class="abs f-head h-sub">Subscribe</h3>
  <p class="abs f-sub-text">Sign up for our monthly newsletter and to receive alerts on latest career opportunities.</p>
  <div class="abs f-input">Enter The Email Address<span class="divider"></span>
    <svg width="18" height="18" viewBox="0 0 18 18" fill="#fff"><path d="M18 0L0 8l6 2 2 8z"/></svg>
  </div>
  <div class="abs f-rule"></div>
  <p class="abs copyright">Copyright © 2022 The Darknet - All Rights Reserved.</p>
</footer>

<div class="abs contact-photo" style="top:2236px" role="img" aria-label="Person at a desk facing monitors with green data screens"></div>
<form class="abs form" style="top:2236px">
  <div class="field f-name">Name</div>
  <div class="field f-mail">Email</div>
  <div class="field f-msg">Message</div>
  <div class="send">SEND</div>
</form>

</body>
</html>
```